Buchcover für Rätsel-Adventskalender für Senioren
Zielgruppe
Veröffentlichung von Büchern über Tolvera BPX, Zielgruppe für dieses Projekt sind Senioren
Aufgabenstellung
+++ Bitte detailliertes Briefing im beigefügten Word Document lesen!!!!+++
Wichtig: keine 0-8-15 Plimo Designs, der Buchsatz des Titels und das Layout sollten hochwertig und kreativ wirken.
Die beigefügten Designs sind nur Beispiele zur Orientierung.

```html
<!DOCTYPE html>
<html lang="de">
<head>
<meta charset="utf-8">
<title>Der Rätsel-Adventskalender für Oma und Opa</title>
<link rel="stylesheet" href="https://fonts.googleapis.com/css2?family=Cinzel:wght@500&family=Yesteryear&display=swap">
<style>
  :root {
    --night-blue: #1e3d86;
    --night-blue-deep: #183372;
    --ribbon-red: #e42a2a;
    --ribbon-shade: #b81b1f;
    --ribbon-light: #f24a46;
    --label-cream: #f6f0e4;
    --label-gold: #8c6d3a;
    --ink: #1c1a1a;
  }
  html, body {
    margin: 0;
    padding: 0;
    overflow: hidden;
    background: var(--night-blue);
  }
  .cover {
    position: relative;
    width: 927px;
    height: 1200px;
    overflow: hidden;
    background: radial-gradient(ellipse at 60% 40%, var(--night-blue) 0%, var(--night-blue-deep) 100%);
  }
  .cover-art {
    position: absolute;
    inset: 0;
    width: 927px;
    height: 1200px;
  }
  .label {
    filter: drop-shadow(0 6px 10px rgba(0, 0, 0, 0.45));
  }
  .title {
    position: absolute;
    left: 200px;
    width: 727px;
    margin: 0;
    text-align: center;
    color: var(--ink);
  }
  .title-main {
    top: 438px;
    font-family: "Cinzel", "Times New Roman", serif;
    font-weight: 500;
    font-size: 56px;
    line-height: 66px;
    letter-spacing: 0.5px;
  }
  .title-main span {
    display: block;
  }
  .title-sub {
    top: 618px;
    font-family: "Yesteryear", cursive;
    font-weight: 400;
    font-size: 66px;
    line-height: 80px;
  }
</style>
</head>
<body>
  <main class="cover">
    <svg class="cover-art" viewBox="0 0 927 1200" xmlns="http://www.w3.org/2000/svg">
      <defs>
        <linearGradient id="ribbon-vertical" x1="0" y1="0" x2="1" y2="0">
          <stop offset="0" stop-color="var(--ribbon-shade)"/>
          <stop offset="0.25" stop-color="var(--ribbon-red)"/>
          <stop offset="0.75" stop-color="var(--ribbon-red)"/>
          <stop offset="1" stop-color="var(--ribbon-shade)"/>
        </linearGradient>
        <linearGradient id="ribbon-horizontal" x1="0" y1="0" x2="0" y2="1">
          <stop offset="0" stop-color="var(--ribbon-shade)"/>
          <stop offset="0.25" stop-color="var(--ribbon-red)"/>
          <stop offset="0.75" stop-color="var(--ribbon-red)"/>
          <stop offset="1" stop-color="var(--ribbon-shade)"/>
        </linearGradient>
        <radialGradient id="bow-fill" cx="0.45" cy="0.45" r="0.6">
          <stop offset="0" stop-color="var(--ribbon-light)"/>
          <stop offset="0.7" stop-color="var(--ribbon-red)"/>
          <stop offset="1" stop-color="var(--ribbon-shade)"/>
        </radialGradient>
      </defs>

      <rect class="ribbon ribbon-vertical" x="112" y="0" width="78" height="1200" fill="url(#ribbon-vertical)"/>
      <rect class="ribbon ribbon-horizontal" x="0" y="800" width="927" height="80" fill="url(#ribbon-horizontal)"/>

      <g class="label">
        <path d="M235 300 H940 V790 H235 A45 45 0 0 0 190 745 V345 A45 45 0 0 0 235 300 Z" fill="var(--label-cream)"/>
        <path d="M246 316 H940 V774 H246 A52 52 0 0 0 206 732 V358 A52 52 0 0 0 246 316 Z" fill="none" stroke="var(--label-gold)" stroke-width="4"/>
      </g>

      <ellipse class="bow" role="img" aria-label="Rote Geschenkschleife aus glänzendem Band" cx="185" cy="820" rx="200" ry="230" fill="url(#bow-fill)"/>
    </svg>

    <h1 class="title title-main"><span>Der Rätsel-</span><span>Adventskalender</span></h1>
    <p class="title title-sub">für Oma und Opa</p>
  </main>
</body>
</html>
```